Medical Company in need of Modern business card design for new Wound Care clinic.

Modern business card design for our Woundcare company. Logo and description of services can be found on our website; https://www.tovrel-woundcare.com/

```html
<!DOCTYPE html>
<html lang="en">
<head>
<meta charset="utf-8">
<title>Tovrel Woundcare – Business Card</title>
<link href="https://fonts.googleapis.com/css2?family=Poppins:wght@300;400;600&display=swap" rel="stylesheet">
<style>
  :root {
    --stage: #2b2b2b;
    --card: #1b1b1b;
    --ink: #f2f2f2;
    --gold: #e3a93a;
    --gold-light: #f6c25c;
    --gold-deep: #c98e22;
    --rule: #5a5a5a;
  }
  * { margin: 0; padding: 0; box-sizing: border-box; }
  html, body { width: 1200px; height: 689px; overflow: hidden; }
  body {
    background: var(--stage);
    font-family: "Poppins", sans-serif;
    color: var(--ink);
    position: relative;
  }
  .card {
    position: absolute;
    width: 540px;
    height: 309px;
    border-radius: 18px;
    background: var(--card);
    overflow: hidden;
    box-shadow: 0 18px 40px rgba(0,0,0,.45);
  }
  .card--back { left: 36px; top: 190px; }
  .card--front { left: 624px; top: 190px; }

  /* Back: services */
  .services {
    list-style: none;
    position: absolute;
    right: 34px;
    top: 38px;
    text-align: right;
    font-size: 15px;
    font-weight: 300;
    line-height: 1.55;
  }
  .services li { position: relative; padding-right: 18px; }
  .services li::after {
    content: "";
    position: absolute;
    right: 0;
    top: 8px;
    width: 7px;
    height: 7px;
    background: var(--gold);
  }
  .services li.continued::after { display: none; }

  /* Front */
  .brand {
    position: absolute;
    left: 30px;
    top: 150px;
    display: flex;
    align-items: center;
    gap: 9px;
    color: var(--gold);
    font-size: 15px;
    font-weight: 400;
    letter-spacing: 2.5px;
    text-transform: uppercase;
    white-space: nowrap;
  }
  .brand__mark { width: 9px; height: 9px; background: var(--gold); flex: none; }
  .divider {
    position: absolute;
    left: 268px;
    top: 42px;
    width: 1px;
    height: 168px;
    background: var(--rule);
  }
  .contact { position: absolute; left: 290px; top: 44px; }
  .contact__name {
    color: var(--gold);
    font-weight: 600;
    font-size: 18px;
    letter-spacing: .5px;
    text-transform: uppercase;
    line-height: 1.1;
  }
  .contact__role { font-size: 13px; font-weight: 300; margin-bottom: 14px; }
  .contact__row {
    display: flex;
    align-items: center;
    gap: 8px;
    font-size: 12.5px;
    font-weight: 300;
    line-height: 1.6;
  }
  .contact__row svg { width: 12px; height: 12px; flex: none; fill: none; stroke: var(--gold); stroke-width: 1.6; }
  .contact__web em { font-style: normal; color: var(--gold); }
  .contact__address { font-size: 12.5px; font-weight: 300; line-height: 1.4; margin-top: 12px; }

  .band-rule {
    position: absolute;
    left: 0; right: 0;
    bottom: 46px;
    height: 2px;
    background: var(--gold);
  }
  .band {
    position: absolute;
    left: 0; right: 0; bottom: 0;
    height: 40px;
    background: linear-gradient(90deg, var(--gold-deep), var(--gold-light) 55%, var(--gold));
  }
</style>
</head>
<body>

  <section class="card card--back" aria-label="Card back: services">
    <ul class="services">
      <li>Hyperbaric Oxygen Therapy (HBO)</li>
      <li>Debridement</li>
      <li>Advanced Wound Dressings</li>
      <li>Bio-engineered Skin Substitutes</li>
      <li>Compression Therapy</li>
      <li class="continued">and Edema Management</li>
    </ul>
  </section>

  <section class="card card--front" aria-label="Card front: contact">
    <div class="brand"><span class="brand__mark"></span><span>Tovrel Woundcare</span></div>
    <div class="divider"></div>
    <div class="contact">
      <p class="contact__name">Marcus Hale</p>
      <p class="contact__role">Managing Director</p>
      <p class="contact__row">
        <svg viewBox="0 0 12 12"><path d="M2 1.5l2 .3.8 2.2-1.2 1a6 6 0 0 0 3.4 3.4l1-1.2 2.2.8.3 2c-4.5.6-9.1-4-8.5-8.5z"/></svg>
        <span>044-555 018 220</span>
      </p>
      <p class="contact__row">
        <svg viewBox="0 0 12 12"><rect x="1" y="2.5" width="10" height="7"/><path d="M1 2.5l5 4 5-4"/></svg>
        <span>info@webname.com</span>
      </p>
      <p class="contact__row contact__web">
        <svg viewBox="0 0 12 12"><circle cx="6" cy="6" r="5"/><path d="M1 6h10M6 1c-2.5 3-2.5 7 0 10M6 1c2.5 3 2.5 7 0 10"/></svg>
        <span>www.<em>websitename</em>.com</span>
      </p>
      <p class="contact__address">421, Address line goes here<br>45452,Country Name</p>
    </div>
    <div class="band-rule"></div>
    <div class="band"></div>
  </section>

</body>
</html>
```